New Signage Design Project for Qb Dale Outworks *

Im Looking for yard design with our logo, number, website, services & credentials. Each Yard sign will be for 3 different titles...

Example 1: New Roof Coming Soon (Title) This Yardsign is for projects before we start them... Letting neighbors know why we are going to be there.
Example 2: New Roof In progress (Title) This Yardsign is for during the process of the work.. letting neighbors know what we working on!!
Example 3: This Design is only for the customer that says a title NEW ROOF INSTALL SATISFIED CUSTOMER ON THIS DESIGN I DONT NEED SERVICES JSUT LOGO AND THE TITLE

Target Market(s)

Customers

Industry/Entity Type

Roofing

Font styles to use
Serif
Sans Serif

Colors
33b8a4
5c5c5c

Requirements
Must have
• -LOGO
• -WEBSITE
• -NUMBER
• -TITLES
• -SERVICES (ROOFING, GUTTERS, PAINTING, PRESSURE WASHING, EXTERIOR DESIGN.)
• -CREDENTIALS
• -HOUSE SHAPE DESIGN
• -LOGO COLORS
• -NOT BUSY BUT CLEAN AND SHARP
• -MATTE COLORS
Nice to have
• Easy To read, Eye Catchy, Clean Design, logo colors, titles
Should not have
• not Busy,

```html
<!DOCTYPE html>
<html lang="en">
<head>
<meta charset="utf-8">
<title>Qb Dale Outworks — New Roof Install Yard Sign</title>
<link href="https://fonts.googleapis.com/css2?family=Oswald:wght@200;300&family=Montserrat:wght@400;500&family=Merriweather:wght@400;700&display=swap" rel="stylesheet">
<style>
  :root {
    --bg-deep: #10443f;
    --bg-glow: #1c8a7c;
    --sign-dark: #333335;
    --teal: #1f9a89;
    --band-grey: #58585a;
    --tagline-grey: #8a8a8c;
    --photo-light: #d9d4cf;
    --photo-warm: #b98f7d;
    --white: #ffffff;
  }
  html, body {
    margin: 0;
    width: 1200px;
    height: 1200px;
    overflow: hidden;
  }
  body {
    background: radial-gradient(circle at 50% 55%, var(--bg-glow) 0%, var(--bg-deep) 75%);
  }
  .yard-sign {
    position: absolute;
    left: 186px;
    top: 114px;
    width: 828px;
    height: 972px;
    filter: drop-shadow(0 8px 14px rgba(0,0,0,0.35));
  }
  .sign-body { fill: var(--sign-dark); }
  .inner-frame { fill: none; stroke: var(--teal); stroke-width: 2; }
  .brand-name { font-family: "Merriweather", serif; font-weight: 700; fill: var(--teal); }
  .brand-line { font-family: "Montserrat", sans-serif; font-weight: 400; fill: var(--tagline-grey); letter-spacing: 2px; }
  .title-new { font-family: "Oswald", sans-serif; font-weight: 200; fill: var(--white); }
  .title-band { fill: var(--teal); }
  .title-roof { font-family: "Montserrat", sans-serif; font-weight: 500; fill: var(--sign-dark); }
  .title-install { font-family: "Montserrat", sans-serif; font-weight: 400; fill: var(--teal); }
  .find-label { font-family: "Montserrat", sans-serif; font-weight: 400; fill: var(--teal); }
  .rule { stroke: var(--tagline-grey); stroke-width: 1.5; }
  .phone { font-family: "Oswald", sans-serif; font-weight: 300; fill: var(--white); }
  .contact-band { fill: var(--band-grey); }
  .contact-text { font-family: "Montserrat", sans-serif; font-weight: 400; fill: var(--white); }
  .contact-icon { fill: none; stroke: var(--teal); stroke-width: 1.6; }
  .social-dot { fill: var(--teal); }
  .divider { stroke: #5a5a5c; stroke-width: 1.5; }
  .badge-listing { fill: #3c66a8; }
  .badge-cert { fill: #c9302c; }
</style>
</head>
<body>
<svg class="yard-sign" viewBox="0 0 690 810" xmlns="http://www.w3.org/2000/svg">
  <defs>
    <linearGradient id="photoTone" x1="0" y1="0" x2="1" y2="1">
      <stop offset="0" stop-color="#3a3a3c"/>
      <stop offset="0.45" stop-color="var(--photo-warm)"/>
      <stop offset="1" stop-color="var(--photo-light)"/>
    </linearGradient>
  </defs>

  <path class="sign-body" d="M197 0 L392 135 L687 135 L687 800 L0 800 L0 125 L62 86 L62 17 L110 17 L110 56 Z"/>
  <path class="inner-frame" d="M197 35 L392 158 L670 158 L670 785 L18 785 L18 146 Z"/>

  <rect x="342" y="0" width="345" height="320" fill="url(#photoTone)" role="img" aria-label="Photo of two smiling satisfied customers giving an OK hand sign"/>

  <!-- brand -->
  <text class="brand-name" x="192" y="205" text-anchor="middle" font-size="34" textLength="210" lengthAdjust="spacingAndGlyphs">QB DALE</text>
  <text class="brand-name" x="192" y="245" text-anchor="middle" font-size="34" textLength="210" lengthAdjust="spacingAndGlyphs">OUTWORKS</text>
  <text class="brand-line" x="192" y="270" text-anchor="middle" font-size="11.5" textLength="206" lengthAdjust="spacingAndGlyphs">ROOFING &amp; EXTERIORS</text>

  <!-- title -->
  <text class="title-new" x="77" y="465" font-size="172" textLength="240" lengthAdjust="spacingAndGlyphs">NEW</text>
  <rect class="title-band" x="337" y="320" width="350" height="90"/>
  <text class="title-roof" x="340" y="401" font-size="98" textLength="273" lengthAdjust="spacingAndGlyphs">ROOF</text>
  <text class="title-install" x="340" y="467" font-size="72" textLength="270" lengthAdjust="spacingAndGlyphs">INSTALL</text>

  <!-- contact -->
  <line class="rule" x1="120" y1="541" x2="203" y2="541"/>
  <line class="rule" x1="493" y1="541" x2="577" y2="541"/>
  <text class="find-label" x="348" y="552" text-anchor="middle" font-size="32" textLength="258" lengthAdjust="spacingAndGlyphs">FIND US HERE</text>
  <text class="phone" x="348" y="640" text-anchor="middle" font-size="98" textLength="462" lengthAdjust="spacingAndGlyphs">503-555-0148</text>

  <rect class="contact-band" x="0" y="658" width="687" height="40"/>
  <g class="contact-icon">
    <rect x="35" y="672" width="20" height="13"/>
    <path d="M35 672 L45 680 L55 672"/>
    <circle cx="367" cy="680" r="8"/>
    <path d="M359 680 H375 M367 672 Q361 680 367 688 Q373 680 367 672"/>
  </g>
  <text class="contact-text" x="64" y="685" font-size="19" textLength="282" lengthAdjust="spacingAndGlyphs">: info@qbdaleoutworks.com</text>
  <text class="contact-text" x="381" y="685" font-size="19" textLength="282" lengthAdjust="spacingAndGlyphs">: www.qbdaleoutworks.com</text>

  <!-- social & credentials -->
  <g class="social-dot">
    <circle cx="163" cy="743" r="12"/>
    <circle cx="197" cy="743" r="12"/>
    <circle cx="231" cy="743" r="12"/>
    <circle cx="266" cy="743" r="12"/>
    <circle cx="300" cy="743" r="12"/>
    <circle cx="335" cy="743" r="12"/>
  </g>
  <line class="divider" x1="372" y1="715" x2="372" y2="772"/>
  <rect class="badge-listing" x="400" y="725" width="24" height="37"/>
  <rect class="badge-cert" x="433" y="725" width="103" height="37"/>
</svg>
</body>
</html>
```